Brochure Design Project

Architectural photography and virtual tour provider for local and national real estate markets. You can use my website for design and image needs. www.larchviewhomeshots.com

```html
<!DOCTYPE html>
<html lang="en">
<head>
<meta charset="utf-8">
<title>Larchview Home Shots – Brochure</title>
<link rel="stylesheet" href="https://fonts.googleapis.com/css2?family=Montserrat:wght@600;700;800;900&family=Open+Sans:ital,wght@0,400;0,600;0,700;1,400&display=swap">
<style>
:root{
  --blue:#1d4fa6;
  --green:#3ba74d;
  --orange:#f0a633;
  --orange-deep:#e8912a;
  --charcoal:#3c3c3e;
  --ink:#333336;
  --muted:#7a7a7e;
  --paper:#ffffff;
  --backdrop:#e6e6e6;
  --badge:#c9ced6;
  --heading:'Montserrat',sans-serif;
  --body:'Open Sans',sans-serif;
}
*{box-sizing:border-box;margin:0;padding:0}
html,body{width:1200px;height:2473px;overflow:hidden}
body{background:var(--backdrop);font-family:var(--body);color:var(--ink)}
.stage{position:relative;width:1200px;height:824px}
.stage:last-child{height:825px}
.page{position:absolute;background:var(--paper);overflow:hidden;box-shadow:0 8px 24px rgba(0,0,0,.14)}
.grid-photo{position:relative}

/* ---------- front cover ---------- */
.cover{position:relative;width:560px;height:725px;background:var(--paper)}
.brand{position:absolute;left:74px;top:30px;display:flex;align-items:center;gap:10px}
.brand-mark{width:30px;height:30px;background:var(--blue)}
.brand-name{font:600 20px var(--body);color:var(--ink);line-height:1}
.brand-tag{display:block;font:400 10px var(--body);color:var(--muted);text-align:right;margin-top:4px}
.formerly{position:absolute;left:84px;top:84px;font:700 12px var(--body);color:var(--blue)}
.mosaic{position:absolute;left:40px;top:108px;width:480px;height:364px;display:grid;grid-template-columns:1fr 1fr 1fr 1fr;grid-template-rows:repeat(6,1fr);gap:5px}
.quality{position:absolute;left:190px;right:36px;top:482px;text-align:center;color:var(--blue)}
.quality-word{font:900 66px var(--heading);letter-spacing:1px;line-height:1}
.quality-sub{font:600 13px var(--body);letter-spacing:3px;margin-top:4px}

.slot{position:absolute;overflow:hidden;background:var(--paper);box-shadow:0 8px 24px rgba(0,0,0,.14)}
.slot .cover{transform:scale(.8929);transform-origin:0 0}

/* ---------- back cover ---------- */
.back{background:var(--charcoal);color:#fff}
.back-title{position:absolute;left:40px;top:66px;text-align:center}
.back-title h2{font:800 30px var(--heading);letter-spacing:1px}
.back-title span{display:block;font:600 9px var(--body);letter-spacing:4px;color:#cfcfcf;margin-top:2px}
.frame{position:absolute;border:6px solid #fff;box-shadow:0 4px 12px rgba(0,0,0,.35)}
.socials{position:absolute;left:0;right:0;top:530px;display:flex;justify-content:center;gap:8px}
.socials i{width:16px;height:16px;border-radius:50%;background:#fff;display:block}
.site{position:absolute;left:0;right:0;top:560px;text-align:center;font:600 13px var(--body);letter-spacing:.5px}

/* ---------- inside spread ---------- */
.spread-heading{position:absolute;left:0;right:0;top:22px;text-align:center;font:800 21px var(--heading);color:var(--blue);letter-spacing:.5px}
.bracket{position:absolute;left:0;top:0}
.features{position:absolute;left:28px;right:28px;top:78px;display:flex;justify-content:space-between}
.feature{width:150px;text-align:center}
.feature .round{width:120px;height:120px;border-radius:50%;margin:0 auto 10px;border:4px solid #fff;box-shadow:0 3px 10px rgba(0,0,0,.25)}
.feature h3{font:800 12.5px var(--heading);color:var(--ink);line-height:1.15}
.feature p{font:400 8.5px var(--body);color:var(--muted);margin-top:6px;line-height:1.4}

.includes{position:absolute;left:0;right:0;top:302px;height:196px;background:var(--green);color:#fff;padding:16px 34px 0}
.includes h3{text-align:center;font:600 15px var(--heading);letter-spacing:1.5px}
.includes-grid{display:grid;grid-template-columns:repeat(3,1fr);margin-top:10px}
.include{text-align:center;padding:8px 6px 9px;border-right:1px solid rgba(255,255,255,.35);line-height:1.4}
.include:nth-child(3n){border-right:none}
.include:nth-child(-n+3){border-bottom:1px solid rgba(255,255,255,.35)}
.include svg{display:block;margin:0 auto 4px}
.include span{font:400 8.5px var(--body);opacity:.9}

.testimonial{position:absolute;left:40px;top:520px;width:270px;color:var(--muted)}
.testimonial .mark{font:700 40px Georgia,serif;color:#b5b5b5;line-height:.6;display:block}
.testimonial p{font:italic 400 11px var(--body);line-height:1.45;margin:8px 0 8px 22px}
.testimonial .author{font:400 9px var(--body);margin-left:22px}
.testimonial .mark.end{text-align:right}
.divider{position:absolute;left:330px;top:528px;width:1px;height:130px;background:#cfcfcf}
.badges{position:absolute;left:352px;top:560px;width:150px;display:flex;flex-wrap:wrap;gap:10px}
.badge{width:70px;height:26px;border-radius:4px;background:var(--badge)}
.badge.small{width:26px}

/* packages */
.band{position:absolute;left:0;right:0}
.band.orange{top:78px;height:168px;background:var(--orange);clip-path:polygon(0 0,100% 0,100% 78%,0 100%)}
.band.dark{top:388px;height:140px;background:var(--charcoal);clip-path:polygon(0 14%,100% 0,100% 88%,0 100%)}
.pkg{position:absolute;width:220px}
.pkg h4{font:800 13px var(--heading);letter-spacing:.3px;line-height:1}
.pkg ul{list-style:none;margin-top:6px}
.pkg li{font:400 8.5px var(--body);line-height:1.45}
.pkg li::before{content:"• "}
.price{display:inline-block;margin-top:7px;padding:3px 18px;border-radius:12px;font:700 11px var(--body)}
.on-orange{color:#fff}
.on-orange .price{background:var(--orange-deep);color:#fff}
.on-white{color:var(--ink)}
.on-white .price{background:var(--charcoal);color:#fff}
.on-white.accent h4{color:var(--orange-deep)}
.on-white.accent .price{background:var(--orange)}
.on-dark{color:#fff}
.on-dark .price{background:#5a5a5d;color:#fff}
.extras{position:absolute;left:300px;top:540px;width:200px}
.extras h4{font:800 13px var(--heading);color:var(--ink)}
.extras dl{display:grid;grid-template-columns:1fr auto;margin-top:6px;row-gap:2px}
.extras dt,.extras dd{font:400 9px var(--body);color:var(--ink)}
</style>
</head>
<body>

<section class="stage">
  <div class="page" style="left:320px;top:50px;width:560px;height:725px">
    <div class="cover">
      <div class="brand">
        <span class="brand-mark"></span>
        <div><span class="brand-name">Larchview Home Shots</span><span class="brand-tag">become noticed...</span></div>
      </div>
      <div class="formerly">formerly Ridgecrest Home Tours</div>
      <div class="mosaic">
        <div class="grid-photo" role="img" aria-label="Bright open living room interior" style="grid-column:1/3;grid-row:1/3;background:linear-gradient(135deg,#e9e6e0,#9d968c)"></div>
        <div class="grid-photo" role="img" aria-label="Bedroom with red accents" style="grid-column:3;grid-row:1;background:linear-gradient(135deg,#b84a3c,#5a4a44)"></div>
        <div class="grid-photo" role="img" aria-label="Warm dining room" style="grid-column:4;grid-row:1;background:linear-gradient(135deg,#c9a88a,#6e5240)"></div>
        <div class="grid-photo" role="img" aria-label="Kitchen with wood cabinets" style="grid-column:1;grid-row:3/5;background:linear-gradient(160deg,#d9c7b0,#8a4e30)"></div>
        <div class="grid-photo" role="img" aria-label="Modern grey dining area" style="grid-column:2;grid-row:3/5;background:linear-gradient(160deg,#d8d6d2,#6f6b66)"></div>
        <div class="grid-photo" role="img" aria-label="Home exterior with pool and palm trees" style="grid-column:3/5;grid-row:2/5;background:linear-gradient(180deg,#8db6de 0%,#c8b79e 45%,#5aa0c8 75%,#4f7a3e 100%)"></div>
        <div class="grid-photo" role="img" aria-label="Wine room shelving" style="grid-column:1;grid-row:5;background:linear-gradient(135deg,#7a4e30,#3a2418)"></div>
        <div class="grid-photo" role="img" aria-label="Kitchen island at dusk" style="grid-column:2;grid-row:5/7;background:linear-gradient(160deg,#a89a8a,#3f3a36)"></div>
        <div class="grid-photo" role="img" aria-label="Backyard pool with fountain" style="grid-column:1;grid-row:6;background:linear-gradient(135deg,#3a78c0,#123a6a)"></div>
        <div class="grid-photo" role="img" aria-label="Lit pool at night" style="grid-column:3/5;grid-row:5/7;background:linear-gradient(180deg,#1b2b4a,#3a5a7a 60%,#c8a050)"></div>
      </div>
      <div class="quality"><div class="quality-word">QUALITY</div><div class="quality-sub">YOU CAN SEE</div></div>
    </div>
  </div>
</section>

<section class="stage">
  <div class="page back" style="left:100px;top:88px;width:500px;height:647px">
    <div class="back-title"><h2>PROFESSIONAL</h2><span>PHOTOGRAPHERS</span></div>
    <div class="frame" role="img" aria-label="House exterior with palm trees under blue sky" style="left:36px;top:150px;width:430px;height:220px;transform:rotate(-5deg);background:linear-gradient(180deg,#6fa3d8 0%,#a9c9e6 45%,#d2bd94 65%,#6e8a48 100%)"></div>
    <div class="frame" role="img" aria-label="Living room interior" style="left:190px;top:350px;width:110px;height:75px;transform:rotate(-5deg);background:linear-gradient(135deg,#d9cfbf,#8a7a66)"></div>
    <div class="frame" role="img" aria-label="Bedroom interior" style="left:310px;top:330px;width:120px;height:82px;transform:rotate(-5deg);background:linear-gradient(135deg,#c08a60,#5a3a2a)"></div>
    <div class="frame" role="img" aria-label="Dining room interior" style="left:60px;top:380px;width:110px;height:72px;transform:rotate(-5deg);background:linear-gradient(135deg,#a8403a,#4a2a28)"></div>
    <div class="socials"><i></i><i></i><i></i><i></i></div>
    <div class="site">www.larchviewhomeshots.com</div>
  </div>
  <div class="slot" style="left:600px;top:88px;width:500px;height:647px">
    <div class="cover">
      <div class="brand">
        <span class="brand-mark"></span>
        <div><span class="brand-name">Larchview Home Shots</span><span class="brand-tag">become noticed...</span></div>
      </div>
      <div class="formerly">formerly Ridgecrest Home Tours</div>
      <div class="mosaic">
        <div class="grid-photo" role="img" aria-label="Bright open living room interior" style="grid-column:1/3;grid-row:1/3;background:linear-gradient(135deg,#e9e6e0,#9d968c)"></div>
        <div class="grid-photo" role="img" aria-label="Bedroom with red accents" style="grid-column:3;grid-row:1;background:linear-gradient(135deg,#b84a3c,#5a4a44)"></div>
        <div class="grid-photo" role="img" aria-label="Warm dining room" style="grid-column:4;grid-row:1;background:linear-gradient(135deg,#c9a88a,#6e5240)"></div>
        <div class="grid-photo" role="img" aria-label="Kitchen with wood cabinets" style="grid-column:1;grid-row:3/5;background:linear-gradient(160deg,#d9c7b0,#8a4e30)"></div>
        <div class="grid-photo" role="img" aria-label="Modern grey dining area" style="grid-column:2;grid-row:3/5;background:linear-gradient(160deg,#d8d6d2,#6f6b66)"></div>
        <div class="grid-photo" role="img" aria-label="Home exterior with pool and palm trees" style="grid-column:3/5;grid-row:2/5;background:linear-gradient(180deg,#8db6de 0%,#c8b79e 45%,#5aa0c8 75%,#4f7a3e 100%)"></div>
        <div class="grid-photo" role="img" aria-label="Wine room shelving" style="grid-column:1;grid-row:5;background:linear-gradient(135deg,#7a4e30,#3a2418)"></div>
        <div class="grid-photo" role="img" aria-label="Kitchen island at dusk" style="grid-column:2;grid-row:5/7;background:linear-gradient(160deg,#a89a8a,#3f3a36)"></div>
        <div class="grid-photo" role="img" aria-label="Backyard pool with fountain" style="grid-column:1;grid-row:6;background:linear-gradient(135deg,#3a78c0,#123a6a)"></div>
        <div class="grid-photo" role="img" aria-label="Lit pool at night" style="grid-column:3/5;grid-row:5/7;background:linear-gradient(180deg,#1b2b4a,#3a5a7a 60%,#c8a050)"></div>
      </div>
      <div class="quality"><div class="quality-word">QUALITY</div><div class="quality-sub">YOU CAN SEE</div></div>
    </div>
  </div>
</section>

<section class="stage">
  <div class="page" style="left:60px;top:62px;width:540px;height:699px">
    <svg class="bracket" width="540" height="70" aria-hidden="true"><path d="M50 56 L72 36 H192 M348 36 H468 L490 56" fill="none" stroke="var(--blue)" stroke-width="3"/></svg>
    <div class="spread-heading">ABOUT US</div>
    <div class="features">
      <div class="feature">
        <div class="round" role="img" aria-label="Living room at dusk" style="background:linear-gradient(135deg,#3a3a48,#b07a40)"></div>
        <h3>30 Years trusted Experience</h3>
        <p>Proudly serving local brokers and national listing agencies</p>
      </div>
      <div class="feature">
        <div class="round" role="img" aria-label="Bright modern interior" style="background:linear-gradient(135deg,#e4e2de,#8a8884)"></div>
        <h3>Professional Photos</h3>
        <p>• Properties with quality photos sell faster<br>• Stand out against the competition</p>
      </div>
      <div class="feature">
        <div class="round" role="img" aria-label="Aerial view of pool and yard" style="background:linear-gradient(135deg,#6aa8d8,#4a7a48)"></div>
        <h3>Stunning Aerial Images</h3>
        <p>Show the full property and its setting from above</p>
      </div>
    </div>
    <div class="includes">
      <h3>ALL PHOTOGRAPHY TOURS INCLUDE:</h3>
      <div class="includes-grid">
        <div class="include"><svg width="26" height="22" viewBox="0 0 26 22" fill="none" stroke="#fff" stroke-width="1.6"><rect x="1" y="5" width="24" height="16" rx="2"/><circle cx="13" cy="13" r="5"/><path d="M8 5 L10 1 H16 L18 5"/></svg><span>High Quality Photography</span></div>
        <div class="include"><svg width="24" height="22" viewBox="0 0 24 22" fill="none" stroke="#fff" stroke-width="1.6"><circle cx="12" cy="11" r="9.5"/><path d="M12 5 V11 L16 14"/></svg><span>1-2 Business Day Turnaround</span></div>
        <div class="include"><svg width="24" height="22" viewBox="0 0 24 22" fill="#fff"><path d="M12 1 L14.5 8.5 L22 11 L14.5 13.5 L12 21 L9.5 13.5 L2 11 L9.5 8.5Z"/></svg><span>Expert Photo Editing</span></div>
        <div class="include"><svg width="24" height="22" viewBox="0 0 24 22" fill="none" stroke="#fff" stroke-width="1.6"><path d="M2 11 L12 2 L22 11 M5 9 V21 H19 V9"/><rect x="10" y="14" width="4" height="7"/></svg><span>Single Property Site</span></div>
        <div class="include"><svg width="26" height="22" viewBox="0 0 26 22" fill="none" stroke="#fff" stroke-width="1.6"><rect x="1" y="1" width="24" height="15" rx="1.5"/><path d="M9 21 H17 M13 16 V21"/></svg><span>Client Portal 24 Hour Access</span></div>
        <div class="include"><svg width="16" height="22" viewBox="0 0 16 22" fill="none" stroke="#fff" stroke-width="1.6"><rect x="1" y="1" width="14" height="20" rx="2"/><path d="M6 17.5 H10"/></svg><span>Mobile Friendly Gallery</span></div>
      </div>
    </div>
    <div class="testimonial">
      <span class="mark">“</span>
      <p>I love working with Larchview Home Shots. They are great to work with, fast turn around and great attention to detail.</p>
      <div class="author">– Maren Okafor, Broker Associate</div>
      <span class="mark end">”</span>
    </div>
    <div class="divider"></div>
    <div class="badges">
      <div class="badge small"></div>
      <div class="badge"></div>
      <div class="badge"></div>
      <div class="badge"></div>
    </div>
  </div>

  <div class="page" style="left:600px;top:62px;width:540px;height:699px">
    <svg class="bracket" width="540" height="70" aria-hidden="true"><path d="M40 48 L58 36 H100 M440 36 H482 L500 48" fill="none" stroke="var(--blue)" stroke-width="3"/></svg>
    <div class="spread-heading">PHOTOGRAPHY PACKAGES</div>
    <div class="band orange"></div>
    <div class="band dark"></div>

    <div class="pkg on-orange" style="left:40px;top:98px">
      <h4>12 SHOT TOUR</h4>
      <ul><li>Recommended for properties under 1,500 sq ft</li><li>Advanced HDR editing included</li><li>Next day turnaround on all photos</li></ul>
      <span class="price">$105</span>
    </div>
    <div class="pkg on-orange" style="left:300px;top:98px">
      <h4>25 SHOT TOUR</h4>
      <ul><li>Recommended for properties up to 3,000 sq ft</li><li>Advanced HDR editing included</li><li>Next day turnaround on all photos</li></ul>
      <span class="price">$135</span>
    </div>

    <div class="pkg on-white" style="left:40px;top:262px">
      <h4>35 SHOT TOUR</h4>
      <ul><li>Recommended for properties up to 5,000 sq ft</li><li>Advanced HDR editing included</li><li>Next day turnaround on all photos</li></ul>
      <span class="price">$155</span>
    </div>
    <div class="pkg on-white accent" style="left:300px;top:262px">
      <h4>50 SHOT TOUR</h4>
      <ul><li>Recommended for properties over 5,000 sq ft</li><li>Advanced HDR editing included</li><li>Next day turnaround on all photos</li></ul>
      <span class="price">$205</span>
    </div>

    <div class="pkg on-dark" style="left:40px;top:414px">
      <h4>35 SHOT TWILIGHT</h4>
      <ul><li>Twilight images shot at dusk for a striking look</li><li>Advanced HDR editing included</li><li>Next day turnaround on all photos</li></ul>
      <span class="price">$275</span>
    </div>
    <div class="pkg on-dark" style="left:300px;top:406px">
      <h4>AERIALS SHOTS</h4>
      <ul><li>5 to 10 aerial images of home and lot</li><li>Licensed and insured drone pilot</li><li>Next day turnaround on all photos</li></ul>
      <span class="price">$150</span>
    </div>

    <div class="pkg on-white" style="left:40px;top:558px">
      <h4>3D WALKSPACE</h4>
      <ul><li>3D virtual walk through</li><li>Dollhouse and floor plan views</li><li>Next day turnaround on all tours</li></ul>
      <span class="price">$200</span>
    </div>
    <div class="extras">
      <h4>ADDITIONAL SERVICES</h4>
      <dl>
        <dt>Single Property Website</dt><dd>$35</dd>
        <dt>Slide Show Video</dt><dd>$35</dd>
        <dt>2D Floor Plan</dt><dd>$35</dd>
        <dt>Virtual Staging per Image</dt><dd>$35</dd>
        <dt>Same Day Delivery</dt><dd>$35</dd>
        <dt>Object Removal</dt><dd>$35</dd>
      </dl>
    </div>
  </div>
</section>

</body>
</html>
```